brisk-vale.com Real Estate, Investment, Financial corporate

Real Estate, Investment, Financial corporate looking site. Show present a professional firm, with an elegant display. Please see the attached file which includes the logo, palette and fonts.
Updates

We just starting the brief today. ( logo was delayed)

Target Market(s)

Investors, Corporate , B2b

Industry/Entity Type

real-estate investments

Number of Pages Required

3 page

Requirements
Must have
• Dazzling Homepage
Nice to have
• paralex

```html
<!DOCTYPE html>
<html lang="en">
<head>
<meta charset="utf-8">
<title>Brisk-Vale — Investment Management</title>
<link href="https://fonts.googleapis.com/css2?family=Playfair+Display:wght@400;700&family=Mulish:wght@300;400;600;700&display=swap" rel="stylesheet">
<style>
:root{
  --orange:#f26a1b;
  --ink:#141414;
  --dark:#1b1b1b;
  --panel:#232323;
  --text:#333;
  --muted:#777;
  --line:#cfcfcf;
  --white:#fff;
  --serif:'Playfair Display', Georgia, serif;
  --sans:'Mulish', Arial, sans-serif;
}
*{box-sizing:border-box;margin:0;padding:0}
html,body{width:1200px;height:4083px;overflow:hidden}
body{position:relative;background:var(--white);font-family:var(--sans);color:var(--text)}
.abs{position:absolute}
.btn{position:absolute;background:var(--orange);color:#fff;font:600 12px var(--sans);text-transform:uppercase;display:flex;align-items:center;justify-content:center;letter-spacing:.2px}
.serif{font-family:var(--serif);font-weight:400}
.photo{position:absolute}

/* hero */
.hero{position:absolute;left:0;top:0;width:1200px;height:615px;background:#161616}
.hero-photo{left:363px;top:0;width:837px;height:563px;background:radial-gradient(ellipse at 45% 45%,#6d7686 0%,#2d3a5c 45%,#1a2542 100%)}
.logo{left:111px;top:18px;color:#fff;font:700 20px var(--serif);letter-spacing:.5px}
.nav{top:21px;color:#fff;font:400 13px var(--sans)}
.nav-cta{left:970px;top:10px;width:118px;height:40px}
.hero-kicker{left:111px;top:191px;color:#fff;font:400 16px var(--sans)}
.hero-title{left:110px;top:210px;color:#fff;font-size:40px;white-space:nowrap}
.hero-copy{left:111px;top:270px;width:420px;color:#cfcfcf;font:400 13px/20px var(--sans)}
.hero-cta{left:112px;top:327px;width:119px;height:39px}
.arrow{top:521px;width:31px;height:31px;background:#0e0e0e;display:flex;align-items:center;justify-content:center}
.dots{left:1110px;top:210px;color:#cfd6e6;font:400 11px var(--sans)}
.dots div{display:flex;align-items:center;height:25.5px;gap:8px;justify-content:flex-end;width:62px}
.dots span.l{display:inline-block;width:24px;height:1px;background:#aab3c8}

/* about */
.about-dark{left:363px;top:615px;width:837px;height:571px;background:#141414}
.about-photo{left:112px;top:675px;width:474px;height:450px;background:linear-gradient(135deg,#c9ced4 0%,#7d8c9e 50%,#2f3e57 100%)}
.about-kicker{left:613px;top:755px;color:#fff;font:400 16px var(--sans)}
.about-title{left:612px;top:773px;width:480px;color:#fff;font-size:40px;line-height:43px}
.about-copy{left:613px;top:879px;width:470px;color:#bdbdbd;font:400 13px/22px var(--sans)}
.about-cta{left:613px;top:1003px;width:119px;height:40px}

/* section heads */
.kicker{width:1200px;text-align:center;font:400 16px var(--sans);color:#333}
.head{width:1200px;text-align:center;font-size:41px;color:#222}
.sub{width:1200px;text-align:center;font:400 14px var(--sans);color:#888}

/* services */
.svc-img{top:1308px;width:224px;height:275px;border-radius:14px 14px 0 0}
.svc-title{top:1596px;font-size:18px;color:#333}
.svc-copy{top:1628px;width:224px;color:#888;font:400 12.5px/19px var(--sans)}
.svc-btn{top:1677px;width:119px;height:38px}

/* projects */
.projects{left:0;top:1756px;width:1200px;height:571px;background:linear-gradient(180deg,#242424,#151515)}
.proj{top:1897px;width:308px;height:357px}

/* facts */
.facts{left:0;top:2473px;width:1200px;height:424px;background:linear-gradient(90deg,#1e1e1e,#2b2b2b 45%,#202020)}
.years{left:112px;top:2607px;width:167px;height:156px;border:3px solid var(--orange);color:#fff;font:700 88px/150px var(--sans);text-align:center;letter-spacing:-4px}
.years-copy{left:279px;top:2662px;width:300px;color:#eee;font:400 18px/25px var(--sans)}
.fact{width:224px;height:162px;border:1px solid #5a5a5a;background:rgba(40,40,40,.8);color:#fff;text-align:center}
.fact b{display:block;margin-top:42px;font:700 34px var(--serif)}
.fact span{font:400 14px var(--sans);color:#ddd}

/* blog */
.blog-img{top:3018px;width:308px;height:206px}
.date{top:3211px;width:131px;height:25px;background:#2b2b2b;color:#fff;border-radius:12px;font:600 11.5px/25px var(--sans);text-align:center}
.blog-title{top:3260px;width:300px;font-size:17.5px;line-height:26px;color:#333}
.blog-copy{top:3320px;width:308px;color:#888;font:400 12.5px/20px var(--sans)}
.blog-btn{top:3371px;width:119px;height:39px}

/* contact */
.footer{left:0;top:3741px;width:1200px;height:342px;background:#171717}
.form-card{left:301px;top:3574px;width:598px;height:195px;background:#fff;box-shadow:0 0 14px rgba(0,0,0,.06)}
.field{position:absolute;border:1px solid var(--line);font:400 11.5px var(--sans);color:#666;padding:12px 12px}
.submit{left:602px;top:3692px;width:251px;height:41px}

/* footer */
.f-head{top:3810px;color:var(--orange);font-size:18px}
.f-text{color:#ddd;font:400 12.5px/20px var(--sans)}
.f-text a{color:var(--orange);font-size:10px;text-decoration:none}
.vline{top:3810px;width:1px;height:140px;background:#3a3a3a}
.badge{top:3936px;width:118px;height:52px;border:1px solid #555;display:flex;align-items:center;justify-content:center}
.social{left:980px;display:flex;align-items:center;gap:12px;color:#ddd;font:400 13px var(--sans)}
.social i{width:36px;height:36px;border-radius:50%;border:1px solid #666;display:block}
.copy{left:0;top:4030px;width:1200px;text-align:center;color:#777;font:400 11.5px var(--sans)}
.copy b{color:#ccc;font-weight:400}
</style>
</head>
<body>

<section class="hero">
  <div class="photo hero-photo" role="img" aria-label="Businessman's hands framing a miniature city skyline"></div>
  <div class="abs logo">BRISK-VALE</div>
  <nav>
    <span class="abs nav" style="left:702px">HOME</span>
    <span class="abs nav" style="left:788px">ABOUT</span>
    <span class="abs nav" style="left:879px">SERVICES</span>
    <span class="btn nav-cta">Contact Us</span>
  </nav>
  <div class="abs hero-kicker">Personalised Services in</div>
  <h1 class="abs hero-title serif">Investment Management</h1>
  <p class="abs hero-copy">Sed ut perspiciatis unde omnis iste natus error sit voluptatem accusantium doloremque laudantium</p>
  <span class="btn hero-cta">Contact Us</span>
  <div class="abs arrow" style="left:327px"><svg width="10" height="10" viewBox="0 0 10 10"><path d="M6.5 1.5 3 5l3.5 3.5" stroke="#fff" fill="none" stroke-width="1.4"/></svg></div>
  <div class="abs arrow" style="left:366px"><svg width="10" height="10" viewBox="0 0 10 10"><path d="M3.5 1.5 7 5 3.5 8.5" stroke="#fff" fill="none" stroke-width="1.4"/></svg></div>
  <div class="abs dots">
    <div>1<span class="l" style="width:42px"></span></div>
    <div>2<span class="l"></span></div>
    <div>3<span class="l"></span></div>
    <div>4<span class="l"></span></div>
    <div>5<span class="l"></span></div>
    <div>6<span class="l"></span></div>
  </div>
</section>

<section>
  <div class="abs about-dark"></div>
  <div class="photo about-photo" role="img" aria-label="Smiling consultant in a meeting with a client"></div>
  <div class="abs about-kicker">We Assist Both Corporate</div>
  <h2 class="abs about-title serif">Innovation from a proven Team</h2>
  <p class="abs about-copy">Sed ut perspiciatis unde omnis iste natus error sit voluptatem accusantium doloremque laudantium, totam rem aperiam, eaque ipsa quae ab illo inventore veritatis et quasi architecto beatae vitae dicta sunt explicabo. Nemo enim ipsam voluptatem quia voluptas sit aspernatur aut odit aut fugit</p>
  <span class="btn about-cta">About Us</span>
</section>

<section>
  <div class="abs kicker" style="top:1223px">What we do</div>
  <h2 class="abs head serif" style="top:1240px">Our Services</h2>

  <div class="photo svc-img" style="left:112px;background:linear-gradient(160deg,#c98a6a,#e9e4df 60%,#b9b4ae)" role="img" aria-label="Businesswoman reviewing documents"></div>
  <h3 class="abs svc-title serif" style="left:112px">Denouncing Pleasure</h3>
  <p class="abs svc-copy" style="left:112px">Sed ut perspiciatis unde omnis iste natus error sit voluptatem</p>
  <span class="btn svc-btn" style="left:112px">Read More</span>

  <div class="photo svc-img" style="left:363px;background:linear-gradient(160deg,#3d3a36,#8d8c8c 45%,#1f1d1b)" role="img" aria-label="Team presenting charts on a screen"></div>
  <h3 class="abs svc-title serif" style="left:363px">Minima Veniam</h3>
  <p class="abs svc-copy" style="left:363px">Sed ut perspiciatis unde omnis iste natus error sit voluptatem</p>
  <span class="btn svc-btn" style="left:363px">Read More</span>

  <div class="photo svc-img" style="left:613px;background:linear-gradient(160deg,#6b5a4c,#a9a6a2 50%,#4a3e34)" role="img" aria-label="Top view of colleagues working at a round table"></div>
  <h3 class="abs svc-title serif" style="left:613px">Human Happiness</h3>
  <p class="abs svc-copy" style="left:613px">Sed ut perspiciatis unde omnis iste natus error sit voluptatem</p>
  <span class="btn svc-btn" style="left:613px">Read More</span>

  <div class="photo svc-img" style="left:864px;background:linear-gradient(160deg,#e6e3df,#c9bcae 55%,#8a6d52)" role="img" aria-label="Woman thinking at a laptop"></div>
  <h3 class="abs svc-title serif" style="left:864px">Ratione Voluptatem</h3>
  <p class="abs svc-copy" style="left:864px">Sed ut perspiciatis unde omnis iste natus error sit voluptatem</p>
  <span class="btn svc-btn" style="left:864px">Read More</span>
</section>

<section>
  <div class="abs projects"></div>
  <h2 class="abs head serif" style="top:1818px;color:#fff">Recent Projects</h2>
  <div class="photo proj" style="left:112px;background:linear-gradient(150deg,#e8ecef,#9aa4ad 55%,#3e4852)" role="img" aria-label="Architectural model of a residential tower"></div>
  <div class="photo proj" style="left:447px;background:linear-gradient(150deg,#e9d6b8,#b78c5e 50%,#6b4a2e)" role="img" aria-label="Model house in front of a business meeting"></div>
  <div class="photo proj" style="left:780px;background:linear-gradient(150deg,#cfd8dc,#8d9a9f 50%,#3e4448)" role="img" aria-label="Professionals discussing a building model"></div>
</section>

<section>
  <h2 class="abs head serif" style="top:2361px">Interesting Facts</h2>
  <p class="abs sub" style="top:2416px">Sed ut perspiciatis unde omnis iste natus error sit voluptatem accusantium</p>
  <div class="abs facts" role="img" aria-label="Darkened background of a businessman in a suit"></div>
  <div class="abs years">15</div>
  <p class="abs years-copy">Years transforming places and creating plans that improve life...</p>
  <div class="abs fact" style="left:613px;top:2509px"><b>220</b><span>Certified Engineers</span></div>
  <div class="abs fact" style="left:864px;top:2509px"><b>220</b><span>Certified Engineers</span></div>
  <div class="abs fact" style="left:613px;top:2701px"><b>220</b><span>Certified Engineers</span></div>
  <div class="abs fact" style="left:864px;top:2701px"><b>220</b><span>Certified Engineers</span></div>
</section>

<section>
  <h2 class="abs head serif" style="top:2945px">Latest Blog Post</h2>

  <div class="photo blog-img" style="left:112px;background:linear-gradient(150deg,#8a6a4e,#d9d4cd 50%,#6e5238)" role="img" aria-label="Desk with laptops, charts and a handshake"></div>
  <div class="abs date" style="left:119px">13 July, 2021</div>
  <h3 class="abs blog-title serif" style="left:112px">Everything You Need to Know About Minimalist Design</h3>
  <p class="abs blog-copy" style="left:112px">Sed ut perspiciatis unde omnis iste natus error sit voluptatem accusantium doloremque...</p>
  <span class="btn blog-btn" style="left:112px">Read More</span>

  <div class="photo blog-img" style="left:447px;background:linear-gradient(150deg,#6f8aa6,#c9d4dc 45%,#2f4660)" role="img" aria-label="Businessman with a tablet in a glass office"></div>
  <div class="abs date" style="left:454px">13 July, 2021</div>
  <h3 class="abs blog-title serif" style="left:447px">Everything You Need to Know About Minimalist Design</h3>
  <p class="abs blog-copy" style="left:447px">Sed ut perspiciatis unde omnis iste natus error sit voluptatem accusantium doloremque...</p>
  <span class="btn blog-btn" style="left:447px">Read More</span>

  <div class="photo blog-img" style="left:780px;background:linear-gradient(150deg,#1f2f5a,#5d6678 50%,#2a2622)" role="img" aria-label="Colleagues meeting around a table"></div>
  <div class="abs date" style="left:787px">13 July, 2021</div>
  <h3 class="abs blog-title serif" style="left:780px">Everything You Need to Know About Minimalist Design</h3>
  <p class="abs blog-copy" style="left:780px">Sed ut perspiciatis unde omnis iste natus error sit voluptatem accusantium doloremque...</p>
  <span class="btn blog-btn" style="left:780px">Read More</span>
</section>

<footer>
  <div class="abs footer"></div>
  <h2 class="abs head serif" style="top:3476px">Contact Us</h2>
  <p class="abs sub" style="top:3532px">Sed ut perspiciatis unde omnis iste natus error sit voluptatem accusantium</p>
  <form class="abs form-card">
    <div class="field" style="left:46px;top:21px;width:250px;height:41px">Name:</div>
    <div class="field" style="left:46px;top:69px;width:250px;height:41px">Email:</div>
    <div class="field" style="left:46px;top:118px;width:250px;height:41px">Phone:</div>
    <div class="field" style="left:301px;top:21px;width:251px;height:89px">Message:</div>
  </form>
  <span class="btn submit">Submit</span>

  <h4 class="abs f-head serif" style="left:112px">Company</h4>
  <p class="abs f-text" style="left:112px;top:3848px;width:240px">Sed ut perspiciatis unde omnis iste natus error sit voluptatem accusantium doloremque laudantium <a>Read More...</a></p>
  <div class="abs badge" style="left:112px" role="img" aria-label="Partner badge"><svg width="70" height="16"><rect width="70" height="16" rx="3" fill="#3a3a3a"/></svg></div>
  <div class="abs badge" style="left:246px" role="img" aria-label="Partner badge"><svg width="60" height="16"><rect width="60" height="16" rx="3" fill="#3a3a3a"/></svg></div>

  <h4 class="abs f-head serif" style="left:445px">Sitemap</h4>
  <div class="abs f-text" style="left:445px;top:3848px;line-height:26.5px">Home<br>About Us<br>Services<br>Contact Us</div>
  <div class="abs vline" style="left:587px"></div>

  <h4 class="abs f-head serif" style="left:658px">Contact Us</h4>
  <p class="abs f-text" style="left:658px;top:3848px;width:240px;line-height:16px">27c/4 Lorem ipsum dolor sit amet<br>Harwick 41L UKE</p>
  <p class="abs f-text" style="left:658px;top:3900px">+2 (555) 246 7310</p>
  <p class="abs f-text" style="left:658px;top:3939px">info@briskvale.com</p>
  <div class="abs vline" style="left:924px"></div>

  <h4 class="abs f-head serif" style="left:980px">Follow Us</h4>
  <div class="abs social" style="top:3851px"><i></i>Friendlane</div>
  <div class="abs social" style="top:3895px"><i></i>Chirpline</div>
  <div class="abs social" style="top:3940px"><i></i>Snapframe</div>

  <p class="abs copy">© 2021 <b>Brisk-Vale</b>. All Rights Reserved.</p>
</footer>

</body>
</html>
```